Window cleaning company in need of leaflet design

Family run business requires leaflet design.
Our company uses water fed pole with pure water which is what the leaflet needs to emphasise on (include a background picture of a water fed pole cleaning a window.)

other services we offer which i would like to include are:
• facia/soffit cleaning.
• Conservatory cleans.
• Gutter clearing which is performed by a gutter vacuum pictures of gutters before and after clean are provided to every customer if they require.
• pressure washing

uploaded company logo to be included on leaflet.
number to include is 07942615380
email address is Tbglasswash@mailvento.com
would also like a facebook symbol included to show we are on social media.
Thank you

Font styles to use
Serif
Sans Serif

Colors
00a990
33a6d7
3276b5
3277b5
34a7d8
87cfc6
33b8a4
cfdfed
85acd3

Requirements
Must have
• We use traditional and water fed pole methods of cleaning. So those hard to reach or awkward to clean windows are not a problem. No need for ladders.

Our water fed pole system uses 100% pure water. This is water that has been de-ironised and de-mineralised to ensue it’s perfectly pure for a spot free finish.

• fully insured

• regular and reliable service
• one off cleans available

Call dean on 07942615380 for a free quote

```html
<!DOCTYPE html>
<html lang="en">
<head>
<meta charset="utf-8">
<title>T.B Glass Wash – Leaflet</title>
<link rel="stylesheet" href="https://fonts.googleapis.com/css2?family=Bebas+Neue&family=Open+Sans:wght@400;600;700&display=swap">
<style>
  :root{
    --navy:#1f2f86;
    --royal:#2b49a8;
    --sky:#33a6d7;
    --steel:#3276b5;
    --ink:#555b63;
    --grey-bar:#b9bcc2;
    --paper:#f5f6f8;
    --page:#e6e8eb;
    --white:#ffffff;
  }
  *{box-sizing:border-box;margin:0;padding:0}
  html,body{width:1024px;height:1200px;overflow:hidden;background:var(--page)}
  .leaflet{position:absolute;left:87px;top:0;width:850px;height:1200px;overflow:hidden;background:var(--paper);font-family:"Open Sans",Arial,sans-serif}
  .leaflet-shapes{position:absolute;inset:0}
  .abs{position:absolute}
  .display{font-family:"Bebas Neue",Impact,sans-serif;font-weight:400;line-height:1}
  .headline{left:30px;top:78px;font-size:60px;color:var(--white)}
  .headline .accent{display:block;color:var(--sky);margin-top:6px}
  .headline-rule{left:30px;top:236px;width:206px;height:7px;background:var(--grey-bar)}
  .subline{left:34px;top:280px;font-size:22px;font-weight:700;color:var(--white);line-height:1.4}
  .brand-name{left:40px;top:556px;font-size:36px;color:var(--navy);font-weight:400;line-height:1.2}
  .features{left:34px;top:620px;list-style:none}
  .features li{font-size:20px;font-weight:700;color:var(--ink);height:30.5px;display:flex;align-items:center}
  .features li::before{content:"";width:15px;height:15px;border-radius:50%;background:var(--royal);margin-right:12px;box-shadow:inset 0 0 0 4px var(--royal);
    background-image:linear-gradient(45deg,transparent 45%,#fff 45%,#fff 58%,transparent 58%)}
  .pure-water{left:30px;top:756px;width:394px;height:125px;border-radius:8px;border:4px solid #dfe3ea;
    background:linear-gradient(180deg,#2f6fd0,#1f3f9a);box-shadow:0 4px 10px rgba(0,0,0,.3);
    color:var(--white);font-size:35px;text-align:center;display:flex;align-items:center;justify-content:center;line-height:1.05}
  .pure-water-note{left:32px;top:902px;font-size:16px;font-weight:600;color:var(--ink);line-height:1.38;white-space:nowrap}
  .based-in{left:32px;top:988px;font-size:36px;color:var(--sky);line-height:1}
  .contact{left:32px;height:26px;font-size:18px;font-weight:700;color:var(--steel);display:flex;align-items:center;gap:12px;line-height:1}
  .contact svg{width:24px;height:24px;flex:none}
  .contact-phone{top:1036px}
  .contact-email{top:1069px}
  .services-tab{left:441px;top:637px;width:404px;height:42px;background:var(--sky);border-radius:4px 4px 0 0;
    color:var(--white);font-size:33px;text-align:center;padding-top:5px;box-shadow:0 3px 6px rgba(0,0,0,.3)}
  .services{left:473px;top:690px;list-style:none}
  .services li{height:55.5px;display:flex;align-items:center;gap:16px;color:var(--white);font-size:19px;font-weight:700;text-shadow:0 2px 3px rgba(0,0,0,.4)}
  .service-icon{width:46px;height:46px;border-radius:50%;border:2px solid #9fb3e6;background:#3a5cc0;display:flex;align-items:center;justify-content:center}
  .service-icon svg{width:24px;height:24px}
  .before-after{left:477px;top:909px;width:330px;height:104px;border:2px solid #d8deea;border-radius:4px;display:flex;gap:4px;background:#d8deea;overflow:hidden}
  .before-after .shot{flex:1;position:relative;overflow:hidden}
  .shot-before{background:linear-gradient(135deg,#4a4f55,#2e3237 60%,#6b5a45)}
  .shot-after{background:linear-gradient(135deg,#5b6168,#3a3f45)}
  .shot .tag{position:absolute;left:-22px;top:10px;transform:rotate(-40deg);background:var(--sky);color:#fff;font-size:11px;font-weight:700;padding:2px 24px}
  .social-mark{left:386px;top:1112px;width:66px;height:66px;border-radius:5px;background:linear-gradient(180deg,#3b79d8,#1e4aa3);border:3px solid #dfe6f2}
  .cta{left:480px;top:1106px;color:var(--white)}
  .cta-title{font-size:36px;font-weight:700;line-height:1.1;text-shadow:0 2px 3px rgba(0,0,0,.35)}
  .cta-line{font-size:23px;display:flex;align-items:center;gap:12px;margin-top:4px}
  .cta-line svg{width:24px;height:24px}
</style>
</head>
<body>
<main class="leaflet">
  <svg class="leaflet-shapes" viewBox="0 0 850 1200" width="850" height="1200">
    <defs>
      <linearGradient id="photoTone" x1="0" y1="0" x2="1" y2="0">
        <stop offset="0" stop-color="#141416"/>
        <stop offset=".45" stop-color="#4a3a36"/>
        <stop offset=".75" stop-color="#9a5a44"/>
        <stop offset="1" stop-color="#b06a4f"/>
      </linearGradient>
      <linearGradient id="panelBlue" x1="0" y1="0" x2="0" y2="1">
        <stop offset="0" stop-color="#2b56c2"/>
        <stop offset="1" stop-color="#1f2f86"/>
      </linearGradient>
      <linearGradient id="footBlue" x1="0" y1="0" x2="1" y2="0">
        <stop offset="0" stop-color="#2f6fd0"/>
        <stop offset="1" stop-color="#1f2f86"/>
      </linearGradient>
    </defs>
    <rect class="hero-photo" role="img" aria-label="Photo: water fed pole brush cleaning an upstairs window on a brick house" x="0" y="0" width="850" height="640" fill="url(#photoTone)"/>
    <rect x="0" y="0" width="850" height="640" fill="#000" opacity=".15"/>
    <path d="M0,455 Q260,405 460,515 L460,640 L0,640Z" fill="var(--sky)"/>
    <path d="M0,475 Q260,425 460,535 L850,535 L850,1200 L0,1200Z" fill="var(--paper)"/>
    <path d="M0,475 Q260,425 460,535" fill="none" stroke="#fff" stroke-width="10"/>
    <rect x="453" y="560" width="380" height="640" fill="url(#panelBlue)"/>
    <path d="M0,1110 Q300,1240 560,1100 T850,1040 L850,1200 L0,1200Z" fill="var(--sky)"/>
    <path d="M0,1140 Q300,1260 560,1120 T850,1065 L850,1200 L0,1200Z" fill="#fff"/>
    <path d="M0,1150 Q300,1270 560,1130 T850,1075 L850,1200 L0,1200Z" fill="url(#footBlue)"/>
    <circle cx="517" cy="500" r="96" fill="#fff"/>
    <circle class="photo-roof" role="img" aria-label="Photo: water fed pole cleaning a conservatory roof" cx="517" cy="500" r="88" fill="#9db3c4"/>
    <circle cx="712" cy="486" r="120" fill="#fff"/>
    <circle class="photo-gutter" role="img" aria-label="Photo: gutter vacuum hose clearing a roof gutter" cx="712" cy="486" r="112" fill="#6b7a5c"/>
  </svg>

  <h1 class="abs display headline">Hard to reach<span class="accent">Windows cleaned</span></h1>
  <div class="abs headline-rule"></div>
  <p class="abs subline">WINDOWS, FRAMES AND SILLS<br>CLEANED EVERY TIME</p>

  <p class="abs brand-name">T.B Glass Wash</p>
  <ul class="abs features">
    <li>Fully Insured</li>
    <li>Regular And Reliable Service</li>
    <li>One Off Cleans Available</li>
    <li>Locally Owned And Operated</li>
  </ul>

  <div class="abs display pure-water">Our water fed pole system<br>uses 100% pure water!</div>
  <p class="abs pure-water-note">This is water that has been de-ironised and<br>de-mineralised to ensue it’s perfectly pure<br>for a spot free finish.</p>

  <h2 class="abs display based-in">Based in Oakridge</h2>
  <p class="abs contact contact-phone">
    <svg viewBox="0 0 24 24"><circle cx="12" cy="12" r="12" fill="var(--navy)"/><path d="M8 6l2 0 1 3-1.5 1a7 7 0 0 0 4 4l1-1.5 3 1 0 2c-5 1-10-4-9-9.5z" fill="#fff"/></svg>
    07942615380
  </p>
  <p class="abs contact contact-email">
    <svg viewBox="0 0 24 24"><circle cx="12" cy="12" r="12" fill="var(--navy)"/><rect x="6" y="8" width="12" height="8" fill="#fff"/><path d="M6 8l6 5 6-5" fill="none" stroke="var(--navy)" stroke-width="1.3"/></svg>
    Tbglasswash@mailvento.com
  </p>

  <h2 class="abs display services-tab">Other services we offer</h2>
  <ul class="abs services">
    <li><span class="service-icon"><svg viewBox="0 0 24 24"><path d="M3 14l9-8 9 8" fill="none" stroke="#fff" stroke-width="2.5"/></svg></span>FACIA/SOFFIT CLEANING</li>
    <li><span class="service-icon"><svg viewBox="0 0 24 24"><path d="M4 10l8-5 8 5v9H4z" fill="none" stroke="#fff" stroke-width="2"/><path d="M8 10v9M12 10v9M16 10v9" stroke="#fff" stroke-width="1.5"/></svg></span>CONSERVATORY CLEANS</li>
    <li><span class="service-icon"><svg viewBox="0 0 24 24"><rect x="7" y="8" width="8" height="12" rx="2" fill="#fff"/><path d="M15 11h5" stroke="#fff" stroke-width="2"/></svg></span>PRESSURE WASHING</li>
    <li><span class="service-icon"><svg viewBox="0 0 24 24"><path d="M4 7h16l-3 5H7z" fill="#fff"/><path d="M11 12v7" stroke="#fff" stroke-width="2.5"/></svg></span>GUTTER CLEARING</li>
  </ul>

  <div class="abs before-after">
    <div class="shot shot-before" role="img" aria-label="Photo: gutter full of debris before clearing"><span class="tag">BEFORE</span></div>
    <div class="shot shot-after" role="img" aria-label="Photo: clean gutter after clearing"><span class="tag">AFTER</span></div>
  </div>

  <div class="abs social-mark" aria-label="Find us on social media"></div>
  <div class="abs cta">
    <p class="cta-title">FOR A FREE QUOTE</p>
    <p class="cta-line">Call Dean
      <svg viewBox="0 0 24 24"><circle cx="12" cy="12" r="10" fill="none" stroke="#fff" stroke-width="2"/><path d="M9 7l2 0 .8 2.5-1.2.8a6 6 0 0 0 3 3l.8-1.2 2.5.8 0 2c-4 .8-8.5-3.5-7.9-7.9z" fill="#fff"/></svg>
      07942615380</p>
  </div>
</main>
</body>
</html>
```